Promotional Post crad

SEE SAMPLE POST CARD <br/><br/>Everything in our lab is manufactured inhouse. No outsourcing !<br/><br/>FULL SERVICE DIGITAL DENTAL LABORATORY<br/><br/>We restore all implants <br/><br/>Implant packages starting from $499<br/><br/>Full contour zirconia crown $99<br/><br/>Build up zirconia crown $179<br/><br/>Implant package promotion starting at 499<br/><br/>Try to make the same design on the back of the card with different parts adding up to the final product

Dentists

```html
<!DOCTYPE html>
<html lang="en">
<head>
<meta charset="utf-8">
<title>Verantis Dental Laboratory – Postcard</title>
<link rel="stylesheet" href="https://fonts.googleapis.com/css2?family=Montserrat:wght@500;600;700;800&family=Oswald:wght@500&family=Noto+Serif:wght@400&display=swap">
<style>
  :root {
    --green: #0bbb3e;
    --green-mid: #139a38;
    --green-dark: #0a6e27;
    --ink: #111111;
    --white: #ffffff;
    --page: #e6e6e6;
    --grey-line: #d9d9d9;
    --stamp: #dcdcdc;
    --tagline: #6b6b6b;
  }
  html, body {
    margin: 0;
    padding: 0;
    width: 736px;
    height: 1200px;
    overflow: hidden;
    background: var(--page);
  }
  .sheet {
    position: relative;
    width: 736px;
    height: 1200px;
  }
  .postcard {
    position: absolute;
    left: 68px;
    width: 600px;
    height: 424px;
    background: var(--white);
    box-shadow: 0 6px 18px rgba(0,0,0,0.25);
    overflow: hidden;
  }
  .postcard--front { top: 150px; }
  .postcard--back { top: 614px; }
  .postcard svg { display: block; width: 100%; height: 100%; }

  .brand-name { font-family: 'Montserrat', sans-serif; font-weight: 800; fill: var(--ink); }
  .brand-tagline { font-family: 'Noto Serif', serif; font-weight: 400; fill: var(--tagline); }
  .headline { font-family: 'Montserrat', sans-serif; font-weight: 800; }
  .headline--dark { fill: var(--ink); }
  .headline--green { fill: var(--green-mid); }
  .subhead { font-family: 'Montserrat', sans-serif; font-weight: 600; fill: #222; }
  .banner-text { font-family: 'Montserrat', sans-serif; font-weight: 700; fill: var(--white); }
  .price { font-family: 'Oswald', sans-serif; font-weight: 500; fill: var(--ink); }
  .price-note { font-family: 'Montserrat', sans-serif; font-weight: 500; fill: var(--green-mid); }
  .contact { font-family: 'Montserrat', sans-serif; font-weight: 500; fill: var(--white); }
  .contact-divider { stroke: var(--white); stroke-width: 2; }
  .icon-ring { fill: none; stroke: var(--green); stroke-width: 3; }
  .icon-glyph { fill: none; stroke: var(--white); stroke-width: 2; }
  .address-line { stroke: var(--grey-line); stroke-width: 2; }
</style>
</head>
<body>
<main class="sheet">

  <!-- Front side -->
  <section class="postcard postcard--front" aria-label="Postcard front">
    <svg viewBox="0 0 946 668" xmlns="http://www.w3.org/2000/svg">
      <defs>
        <linearGradient id="ringGreen" x1="0" y1="0" x2="1" y2="1">
          <stop offset="0" stop-color="#0bbb3e"/>
          <stop offset="1" stop-color="#0a7a2b"/>
        </linearGradient>
        <linearGradient id="footerBlack" x1="0" y1="0" x2="0" y2="1">
          <stop offset="0" stop-color="#3a3a3a"/>
          <stop offset="0.5" stop-color="#111111"/>
          <stop offset="1" stop-color="#000000"/>
        </linearGradient>
        <linearGradient id="photoTone" x1="0" y1="0" x2="1" y2="1">
          <stop offset="0" stop-color="#dfe6ea"/>
          <stop offset="0.5" stop-color="#e8c7b0"/>
          <stop offset="1" stop-color="#7fb6e0"/>
        </linearGradient>
        <clipPath id="frontClip"><rect width="946" height="668"/></clipPath>
      </defs>
      <g clip-path="url(#frontClip)">
        <!-- black footer -->
        <path d="M0,565 Q320,640 660,540 Q820,500 946,470 L946,668 L0,668 Z" fill="url(#footerBlack)"/>
        <!-- left green swoosh -->
        <path d="M0,500 Q230,610 460,565 Q230,620 0,545 Z" fill="var(--green)"/>
        <!-- photo ring -->
        <ellipse cx="790" cy="300" rx="240" ry="210" transform="rotate(-28 790 300)" fill="url(#ringGreen)"/>
        <ellipse cx="796" cy="298" rx="212" ry="184" transform="rotate(-28 796 298)" fill="var(--white)"/>
        <g role="img" aria-label="Photo of a smiling patient during a dental check-up">
          <ellipse cx="806" cy="300" rx="198" ry="172" transform="rotate(-28 806 300)" fill="url(#photoTone)"/>
        </g>
        <!-- top right accent -->
        <path d="M805,100 Q880,140 946,120 L946,88 Q880,120 805,100 Z" fill="var(--green-dark)"/>

        <!-- brand -->
        <rect x="56" y="40" width="30" height="30" fill="var(--green-mid)"/>
        <text class="brand-name" x="100" y="70" font-size="38">verantis</text>
        <text class="brand-tagline" x="170" y="106" font-size="18">made in house</text>

        <!-- headline -->
        <text class="headline headline--dark" x="56" y="170" font-size="42">FULL SERVICE</text>
        <text class="headline headline--green" x="56" y="222" font-size="42">DIGITAL DENTAL</text>
        <text class="headline headline--green" x="56" y="274" font-size="42">LABORATORY</text>

        <!-- banner -->
        <line x1="57" y1="296" x2="57" y2="366" stroke="var(--green-dark)" stroke-width="2"/>
        <path d="M56,310 L432,310 A27,27 0 0 1 432,364 L56,364 Z" fill="var(--green-mid)"/>
        <text class="banner-text" x="70" y="346" font-size="24">WE RESTORE ALL IMPLANTS</text>

        <!-- prices -->
        <text class="price" x="56" y="442" font-size="44">$499</text>
        <text class="price-note" x="158" y="412" font-size="14">Implant packages</text>
        <text class="price-note" x="158" y="430" font-size="14">starting</text>
        <text class="price" x="56" y="514" font-size="44">$179</text>
        <text class="price-note" x="158" y="484" font-size="14">Build up</text>
        <text class="price-note" x="158" y="502" font-size="14">zirconia</text>
        <text class="price-note" x="158" y="520" font-size="14">crown</text>

        <line x1="306" y1="395" x2="306" y2="555" stroke="#999" stroke-width="2"/>

        <text class="price" x="328" y="442" font-size="44">$99</text>
        <text class="price-note" x="424" y="412" font-size="14">Full contour</text>
        <text class="price-note" x="424" y="430" font-size="14">zirconia</text>
        <text class="price-note" x="424" y="448" font-size="14">crown</text>
        <text class="price" x="328" y="512" font-size="44">$499</text>
        <text class="price-note" x="424" y="486" font-size="14">Implant package</text>
        <text class="price-note" x="424" y="504" font-size="14">promotion starting</text>

        <!-- contact -->
        <circle class="icon-ring" cx="72" cy="636" r="14"/>
        <path class="icon-glyph" d="M66,630 q0,12 12,12 l2,-4 -4,-2 -2,2 q-4,-2 -6,-6 l2,-2 -2,-4 Z"/>
        <text class="contact" x="104" y="648" font-size="31">123-456-7898</text>
        <line class="contact-divider" x1="348" y1="622" x2="348" y2="650"/>
        <circle class="icon-ring" cx="394" cy="636" r="14"/>
        <circle class="icon-glyph" cx="394" cy="636" r="8"/>
        <path class="icon-glyph" d="M386,636 H402 M394,628 V644"/>
        <text class="contact" x="428" y="646" font-size="31">www.yoursite.com</text>
      </g>
    </svg>
  </section>

  <!-- Back side -->
  <section class="postcard postcard--back" aria-label="Postcard back">
    <svg viewBox="0 0 946 668" xmlns="http://www.w3.org/2000/svg">
      <defs>
        <radialGradient id="backPhoto" cx="0.62" cy="0.78" r="0.6">
          <stop offset="0" stop-color="#d9d9d9"/>
          <stop offset="1" stop-color="#ffffff"/>
        </radialGradient>
        <linearGradient id="arcGreen" x1="0" y1="0" x2="1" y2="1">
          <stop offset="0" stop-color="#0a7a2b"/>
          <stop offset="0.4" stop-color="#0bbb3e"/>
          <stop offset="1" stop-color="#0bbb3e"/>
        </linearGradient>
        <linearGradient id="backFooter" x1="0" y1="0" x2="0" y2="1">
          <stop offset="0" stop-color="#3a3a3a"/>
          <stop offset="1" stop-color="#000000"/>
        </linearGradient>
        <clipPath id="backClip"><rect width="946" height="668"/></clipPath>
      </defs>
      <g clip-path="url(#backClip)">
        <g role="img" aria-label="Faded black and white photo of a smile with a dental mirror">
          <rect width="946" height="668" fill="url(#backPhoto)"/>
        </g>
        <!-- white left panel -->
        <path d="M0,0 L420,0 Q480,70 470,200 Q440,420 170,668 L0,668 Z" fill="var(--white)"/>
        <!-- green arc -->
        <path d="M0,95 C150,20 440,0 470,180 C490,330 340,520 150,668 L210,668 C400,520 520,340 500,180 C470,-20 140,20 0,75 Z" fill="url(#arcGreen)"/>

        <!-- stamp and address lines -->
        <rect x="845" y="32" width="65" height="62" fill="var(--stamp)"/>
        <line class="address-line" x1="552" y1="120" x2="910" y2="120"/>
        <line class="address-line" x1="552" y1="148" x2="910" y2="148"/>
        <line class="address-line" x1="552" y1="178" x2="910" y2="178"/>
        <line class="address-line" x1="552" y1="207" x2="910" y2="207"/>

        <!-- brand -->
        <rect x="28" y="150" width="26" height="26" fill="var(--green-mid)"/>
        <text class="brand-name" x="66" y="176" font-size="32">verantis</text>
        <text class="brand-tagline" x="126" y="206" font-size="16">made in house</text>

        <text class="subhead" x="28" y="256" font-size="25">FULL SERVICE DIGITAL</text>
        <text class="subhead" x="28" y="288" font-size="25">DENTAL LABORATORY</text>

        <path d="M0,300 L385,300 L348,390 L0,390 Z" fill="var(--green-mid)"/>
        <text class="banner-text" x="32" y="338" font-size="31">WE RESTORE ALL</text>
        <text class="banner-text" x="32" y="378" font-size="31">IMPLANTS</text>

        <text class="price" x="30" y="455" font-size="42">$499</text>
        <text class="price-note" x="130" y="432" font-size="14">Implant packages</text>
        <text class="price-note" x="130" y="450" font-size="14">starting</text>
        <text class="price" x="30" y="516" font-size="42">$179</text>
        <text class="price-note" x="130" y="493" font-size="14">Build up</text>
        <text class="price-note" x="130" y="511" font-size="14">zirconia crown</text>
        <text class="price" x="30" y="578" font-size="42">$99</text>
        <text class="price-note" x="130" y="555" font-size="14">Full contour</text>
        <text class="price-note" x="130" y="573" font-size="14">zirconia crown</text>

        <!-- footer -->
        <path d="M250,668 L325,578 L946,578 L946,668 Z" fill="url(#backFooter)"/>
        <circle class="icon-ring" cx="344" cy="624" r="13"/>
        <path class="icon-glyph" d="M338,618 q0,12 12,12 l2,-4 -4,-2 -2,2 q-4,-2 -6,-6 l2,-2 -2,-4 Z"/>
        <text class="contact" x="372" y="635" font-size="29">123-456-7898</text>
        <line class="contact-divider" x1="590" y1="610" x2="590" y2="638"/>
        <circle class="icon-ring" cx="630" cy="624" r="13"/>
        <circle class="icon-glyph" cx="630" cy="624" r="7"/>
        <path class="icon-glyph" d="M623,624 H637 M630,617 V631"/>
        <text class="contact" x="658" y="633" font-size="29">www.yoursite.com</text>
      </g>
    </svg>
  </section>

</main>
</body>
</html>
```